Ridge 9 Ridge Turbine Rentals Pty Ltd

We are a hire company based on the Gold Coast in Australia, we Hire out Generators to construction sites, music festivals, parties, fetes etc. Anywhere where power is required we can provide it.

Ridge 9 Ridge Turbine Rentals pty Ltd also provides all leads, distribution boards, Qualified Electricians to perform all connections. we offer refuelling services and mechanical services. 24Hr on call service - to an actual english speaking operator.

Slogan ''Power Wherever Whenever"

Industry/Entity Type

Construction

Contact Information for Business Card

M: 0417285963
E: bookings@ridge9ridgeturbinerentals.com.au

```html
<!DOCTYPE html>
<html lang="en">
<head>
<meta charset="utf-8">
<title>Ridge 9 Ridge Turbine Rentals – Business Card</title>
<link rel="stylesheet" href="https://fonts.googleapis.com/css2?family=Open+Sans:wght@400;600&display=swap">
<style>
  :root {
    --backdrop: #e9e6e3;
    --card-light: #2d3a45;
    --card-dark: #1f2a33;
    --text-main: #ffffff;
    --text-soft: #e4e9ee;
    --brand-tone: #9fc3cf;
  }
  * { box-sizing: border-box; margin: 0; padding: 0; }
  html, body { width: 1200px; height: 900px; overflow: hidden; }
  body {
    background: var(--backdrop);
    font-family: "Open Sans", Arial, sans-serif;
    position: relative;
  }
  .card {
    position: absolute;
    width: 556px;
    height: 343px;
    background: radial-gradient(ellipse at 40% 30%, var(--card-light), var(--card-dark) 85%);
    box-shadow: 0 6px 18px rgba(0,0,0,0.25);
    color: var(--text-main);
  }
  .card--front { left: 238px; top: 62px; }
  .card--back  { left: 458px; top: 518px; width: 559px; }

  .brand {
    position: absolute;
    display: flex;
    align-items: center;
    gap: 12px;
    color: var(--brand-tone);
    font-weight: 600;
    text-transform: uppercase;
    line-height: 1.15;
  }
  .brand__dot {
    width: 46px; height: 46px;
    border-radius: 50%;
    background: var(--brand-tone);
    flex: none;
  }
  .card--front .brand { left: 42px; top: 68px; font-size: 17px; }
  .card--back .brand { left: 150px; top: 118px; font-size: 21px; }
  .card--back .brand__dot { width: 58px; height: 58px; }

  .contact {
    position: absolute;
    right: 24px;
    top: 146px;
    text-align: right;
    font-size: 14.5px;
    color: var(--text-soft);
    line-height: 20px;
  }
  .contact__name { font-size: 18px; font-weight: 600; color: var(--text-main); line-height: 24px; }
  .contact__role { margin-bottom: 14px; }
  .contact__address { margin-bottom: 14px; }
  .contact__line { display: flex; justify-content: flex-end; align-items: center; gap: 8px; }
  .contact__icon { width: 11px; height: 11px; flex: none; }
  .contact__icon .fill { fill: var(--text-soft); }
  .contact__icon .cut { fill: none; stroke: var(--card-dark); stroke-width: 2; }

  .slogan {
    position: absolute;
    left: 0; right: 0;
    top: 290px;
    text-align: center;
    font-size: 19px;
    font-weight: 600;
  }
</style>
</head>
<body>
  <section class="card card--front">
    <div class="brand">
      <span class="brand__dot"></span>
      <span>Ridge 9 Ridge<br>Turbine Rentals</span>
    </div>
    <div class="contact">
      <p class="contact__name">Daniel Harper</p>
      <p class="contact__role">Managing Director</p>
      <p class="contact__address">12345, Address Goes Here<br>Country Name, 123456.</p>
      <p class="contact__line">044-123 456 789
        <svg class="contact__icon" viewBox="0 0 24 24"><path class="fill" d="M6.6 10.8a15 15 0 0 0 6.6 6.6l2.2-2.2a1 1 0 0 1 1-.25 11.4 11.4 0 0 0 3.6.57 1 1 0 0 1 1 1V20a1 1 0 0 1-1 1A17 17 0 0 1 3 4a1 1 0 0 1 1-1h3.5a1 1 0 0 1 1 1c0 1.25.2 2.45.57 3.57a1 1 0 0 1-.25 1z"/></svg></p>
      <p class="contact__line">info@webname.com
        <svg class="contact__icon" viewBox="0 0 24 24"><rect class="fill" x="1" y="5" width="22" height="14" rx="1"/><path class="cut" d="M2 6l10 7 10-7"/></svg></p>
      <p class="contact__line">www.websitename.com
        <svg class="contact__icon" viewBox="0 0 24 24"><circle class="fill" cx="12" cy="12" r="11"/><path class="cut" d="M1 12h22M12 1c-5 6-5 16 0 22M12 1c5 6 5 16 0 22"/></svg></p>
    </div>
  </section>

  <section class="card card--back">
    <div class="brand">
      <span class="brand__dot"></span>
      <span>Ridge 9 Ridge<br>Turbine Rentals</span>
    </div>
    <p class="slogan">Power Wherever Whenever</p>
  </section>
</body>
</html>
```